BAYVIEW CARE PLAZA (Medical Clinic)

Our Building is named the "Bayview Care Plaza". We are looking for signs for our 3-story medical arts clinic building. The signs will be located on four locations on the front building face. two signs will be placed on the middle of building ( top and above car port) and one sign on each end wing wall. we are looking for a modern font block letters, elegant, clean and eye catching fonts for the signs and a nice logo as well. it may be back-lighted signage located on the four areas of the building.

Target Market(s)

Medical patients, doctors, public. We live in the tropical island of Guam USA in the Pacific Ocean.

Industry/Entity Type

medical purpose, health facility, doctor's clinic

Colors

Designer to choose colors to be used in the design.

Requirements
Must have
• must complement the colors: Burnished Clay (neutral), Crystal Ball ( dark green), and Holly Glen ( lighther green)
Nice to have
• Back-lighted signs for the 4 areas on the building. Nice to have a logo as well.

```html
<!DOCTYPE html>
<html lang="en">
<head>
<meta charset="utf-8">
<title>Bayview Care Plaza – Sign</title>
<link href="https://fonts.googleapis.com/css2?family=Krona+One&display=swap" rel="stylesheet">
<style>
  :root {
    --wall-teal: #154a55;
    --panel-mist: #d4edf0;
    --ink-deep: #0e2a35;
    --highlight: #ffffff;
    --edge-blue: #2a4f9a;
    --brand-blue: #0d5aa5;
    --network-teal: #27bfb4;
    --network-violet: #7a6fb3;
  }
  html, body {
    margin: 0;
    padding: 0;
    width: 1200px;
    height: 900px;
    overflow: hidden;
    background: var(--wall-teal);
  }
  .sign {
    position: relative;
    width: 1200px;
    height: 900px;
    overflow: hidden;
    background: var(--wall-teal);
  }
  .sign-panel {
    position: absolute;
    inset: 0;
  }
  .network-texture {
    position: absolute;
    left: 416px;
    top: 505px;
    width: 368px;
    height: 393px;
    background:
      radial-gradient(ellipse at 30% 80%, rgba(122,111,179,0.22), transparent 60%),
      radial-gradient(ellipse at 70% 40%, rgba(39,191,180,0.28), transparent 65%),
      linear-gradient(to bottom, rgba(39,191,180,0.05), rgba(39,191,180,0.25));
  }
  .building-name {
    position: absolute;
    left: 0;
    width: 1200px;
    top: 128px;
    margin: 0;
    text-align: center;
    font-family: "Krona One", sans-serif;
    font-weight: 400;
    font-size: 58px;
    line-height: 72px;
    color: var(--ink-deep);
    text-shadow: -4px -5px 0 var(--highlight), 1px 2px 0 var(--edge-blue);
  }
  .building-name span { display: block; }
  .brand-mark {
    position: absolute;
    left: 416px;
    width: 368px;
    top: 668px;
    text-align: center;
    font-family: "Krona One", sans-serif;
    font-size: 74px;
    line-height: 88px;
    color: var(--brand-blue);
  }
</style>
</head>
<body>
  <main class="sign">
    <svg class="sign-panel" width="1200" height="900" viewBox="0 0 1200 900" aria-hidden="true">
      <polygon points="360,0 840,0 840,80 784,578 784,898 416,898 416,578 360,80" fill="var(--panel-mist)"/>
    </svg>
    <div class="network-texture" role="img" aria-label="Decorative network of connected teal, blue and violet dots"></div>
    <h1 class="building-name">
      <span>BAYVIEW</span>
      <span>CARE</span>
      <span>PLAZA</span>
    </h1>
    <div class="brand-mark">BCP</div>
  </main>
</body>
</html>
```